Brenway Productions photography and video creator

I need a business card for my production company. I shoot photography and videography for real estate, adventure sports and businesses

simple not to busy

Colors

Designer to choose colors to be used in the design.

Requirements
Must have
• dara@brenwayproductions.ca
• phone -5803317264
• instagram dara_brenway

```html
<!DOCTYPE html>
<html lang="en">
<head>
<meta charset="utf-8">
<title>Brenway Productions – Business Card</title>
<link rel="stylesheet" href="https://fonts.googleapis.com/css2?family=Arimo:wght@400;700&display=swap">
<style>
  :root {
    --page-bg: #d9d6d2;
    --card-light: #eeeeec;
    --card-mid: #dcdcd9;
    --swoosh: #111111;
    --silver: #c9c9c9;
    --ink: #121212;
    --ink-soft: #3a3a3a;
    --divider: #555555;
  }
  * { margin: 0; padding: 0; box-sizing: border-box; }
  html, body {
    width: 1200px;
    height: 969px;
    overflow: hidden;
    background: var(--page-bg);
    font-family: "Arimo", Arial, sans-serif;
  }
  .card {
    position: absolute;
    left: 157px;
    top: 224px;
    width: 926px;
    height: 524px;
    border-radius: 24px;
    overflow: hidden;
    background: linear-gradient(135deg, var(--card-light), var(--card-mid));
    box-shadow: 0 10px 30px rgba(0,0,0,0.18);
  }
  .card-swooshes {
    position: absolute;
    inset: 0;
  }
  .brand {
    position: absolute;
    left: 100px;
    top: 274px;
    width: 326px;
    display: flex;
    justify-content: center;
    align-items: center;
    gap: 10px;
    color: var(--ink);
    font-size: 24px;
    font-weight: 700;
    line-height: 1.2;
    white-space: nowrap;
  }
  .brand-dot {
    width: 16px;
    height: 16px;
    border-radius: 50%;
    background: var(--ink);
    flex: none;
  }
  .divider {
    position: absolute;
    left: 438px;
    top: 184px;
    width: 2px;
    height: 202px;
    background: var(--divider);
  }
  .contact-block {
    position: absolute;
    left: 488px;
    top: 204px;
    color: var(--ink);
  }
  .person-name {
    font-size: 30px;
    font-weight: 700;
    line-height: 1.1;
  }
  .person-role {
    font-size: 20px;
    color: var(--ink-soft);
    margin-top: 4px;
  }
  .contact-list {
    list-style: none;
    margin-top: 24px;
  }
  .contact-list li {
    display: flex;
    align-items: center;
    gap: 12px;
    font-size: 20px;
    line-height: 26px;
    white-space: nowrap;
  }
  .contact-icon {
    width: 17px;
    height: 17px;
    flex: none;
  }
  .social-dot {
    width: 17px;
    height: 17px;
    border-radius: 50%;
    background: var(--ink);
    flex: none;
  }
</style>
</head>
<body>
  <div class="card">
    <svg class="card-swooshes" width="926" height="524" viewBox="0 0 926 524" aria-hidden="true">
      <path d="M0,0 H440 C290,30 100,110 0,228 Z" fill="var(--swoosh)"/>
      <path d="M0,240 C110,115 280,38 440,6" fill="none" stroke="var(--silver)" stroke-width="3"/>
      <path d="M926,356 C800,445 660,500 523,524 H926 Z" fill="var(--swoosh)"/>
      <path d="M505,518 C660,490 800,430 926,345" fill="none" stroke="var(--silver)" stroke-width="3"/>
    </svg>

    <div class="brand">
      <span class="brand-dot"></span>
      <span class="brand-name">Brenway Productions</span>
    </div>

    <div class="divider"></div>

    <div class="contact-block">
      <div class="person-name">Dara Brenway</div>
      <div class="person-role">President</div>
      <ul class="contact-list">
        <li>
          <svg class="contact-icon" viewBox="0 0 24 24" aria-label="Phone">
            <path d="M6.6 10.8a15.1 15.1 0 0 0 6.6 6.6l2.2-2.2c.3-.3.7-.4 1-.2 1.1.4 2.3.6 3.6.6.6 0 1 .4 1 1V20c0 .6-.4 1-1 1C10.6 21 3 13.4 3 4c0-.6.4-1 1-1h3.5c.6 0 1 .4 1 1 0 1.3.2 2.5.6 3.6.1.3 0 .7-.2 1z" fill="var(--ink)"/>
          </svg>
          <span>5803317264</span>
        </li>
        <li>
          <svg class="contact-icon" viewBox="0 0 24 24" aria-label="Email">
            <rect x="3" y="6" width="18" height="12" fill="var(--ink)"/>
            <path d="M3 6 L12 13 L21 6" fill="none" stroke="var(--card-light)" stroke-width="1.6"/>
          </svg>
          <span>dara@brenwayproductions.ca</span>
        </li>
        <li>
          <span class="social-dot" aria-label="Social handle"></span>
          <span>dara_brenway</span>
        </li>
      </ul>
    </div>
  </div>
</body>
</html>
```